Consulting company needs website design

We need a simple, static website design for our consulting company. We are looking for a general design of the look and feel of the website. Initially, it will have these pages:
- Home
- About us
- Services
- Contact us
We have our own logo which I have attached to the brief.

We are looking for a simple website, with white background and the use of gray (darker) as the main theme. Simple fonts. The website should be responsive so it an be easily red in mobile devices.

As part of the project, we will need to receive at least the following items:
- Individual files with sample text to support the pages outlined above
- Necessary CSS files

Our current website is here: http://www.marlowvane.co/

Here are some examples of other website we like to be used as guideline:
- http://www.tornaviamundo.com/
-

Target Market(s)

Individuals and companies looking to hire our company to provide consulting services.

Industry/Entity Type

It Company

Coding

Coded - Design and coding required

Number of Pages Required

4 page

Font styles to use
Sans Serif

Requirements
Must have
• Main page should have the ability to embed Chirply feed into it.
• We prefer the design to use gray tones.

```html
<!DOCTYPE html>
<html lang="en">
<head>
<meta charset="utf-8">
<title>Marlow Vane Group SAS</title>
<link href="https://fonts.googleapis.com/css2?family=Open+Sans:wght@300;400;600;700&display=swap" rel="stylesheet">
<style>
:root{
  --ink:#333333;
  --muted:#777777;
  --rule:#d9d9d9;
  --white:#ffffff;
  --dark:#4a4a4a;
  --darker:#3a3a3a;
  --footer:#555555;
  --bar:#444444;
  --tweet-bg:#eeeeee;
  --hero-a:#cfd8e3;
  --hero-b:#7f93ad;
  --btn:#3f3f3f;
}
*{box-sizing:border-box;margin:0;padding:0}
html,body{width:1200px;height:2388px;overflow:hidden}
body{font-family:"Open Sans",Arial,sans-serif;color:var(--ink);background:var(--white)}
a{color:inherit;text-decoration:none}

.site-header{height:128px;display:flex;align-items:center;justify-content:space-between;padding:0 80px}
.brand{display:flex;align-items:center;gap:16px}
.brand-dot{width:70px;height:70px;border-radius:50%;background:#cccccc}
.brand-name{font-size:30px;font-weight:400;color:#555;line-height:1.1;width:200px}
.main-nav{display:flex;gap:50px;font-size:18px;color:#999}
.main-nav a.active{color:var(--ink);border-bottom:2px solid var(--ink);padding-bottom:6px}

.hero{height:512px;position:relative;background:linear-gradient(100deg,var(--hero-a) 0%,#b7c4d4 45%,var(--hero-b) 100%)}
.hero-photo{position:absolute;right:0;top:0;width:640px;height:100%;background:linear-gradient(90deg,rgba(160,175,195,0) 0%,#6f7f95 60%,#55657b 100%)}
.hero-copy{position:absolute;left:80px;top:130px}
.hero-title{font-size:48px;font-weight:600;color:var(--darker);line-height:1.25;letter-spacing:1px}
.btn-dark{display:inline-block;margin-top:36px;background:var(--btn);color:var(--white);font-size:18px;padding:14px 26px;letter-spacing:.5px}

.welcome{height:340px;text-align:center;padding-top:72px}
.section-title{font-size:40px;font-weight:400;letter-spacing:1px}
.welcome p{width:860px;margin:22px auto 0;font-size:15px;color:var(--muted);line-height:1.6}
.btn-outline{display:inline-block;margin-top:26px;border:2px solid #666;padding:10px 24px;font-size:18px;letter-spacing:1px}

.services{height:472px;background:linear-gradient(180deg,#5a5a5a,var(--darker));color:var(--white);text-align:center;padding-top:52px}
.service-grid{display:flex;justify-content:center;gap:36px;margin-top:30px}
.service-card{width:232px}
.service-photo{height:136px;background:linear-gradient(135deg,#c9d2dc,#7c8a9c)}
.service-card h3{font-size:20px;font-weight:400;margin-top:12px}
.service-card p{font-size:14px;color:#ddd;line-height:1.45;margin-top:6px}

.news{height:320px;text-align:center;padding-top:44px}
.news-list{display:flex;justify-content:center;gap:60px;margin-top:30px}
.news-item{display:flex;gap:18px;width:420px;text-align:left}
.news-photo{width:200px;height:132px;flex:none;background:linear-gradient(135deg,#2f4e7a,#9ab3cf)}
.news-item p{font-size:14px;line-height:1.5}
.news-date{font-size:12px;color:var(--muted)}
.news-item .more{display:block;font-size:13px;font-weight:700;margin-top:8px}

.tweets{height:396px;background:var(--tweet-bg);text-align:center;padding-top:52px;position:relative}
.tweet-icon{margin:18px auto 0;width:40px;height:40px;border-radius:50%;background:#888}
.tweet-arrow{position:absolute;top:210px;width:54px;height:54px;border-radius:50%;background:var(--darker);display:flex;align-items:center;justify-content:center}
.tweet-arrow.prev{left:140px}.tweet-arrow.next{right:140px}
.tweet-body{width:760px;margin:24px auto 0;font-size:16px;line-height:1.75;color:#555}
.tweet-author{margin-top:14px;font-size:16px;font-weight:600}
.tweet-date{margin-top:16px;font-size:14px;color:var(--muted)}

.site-footer{height:292px;background:var(--footer);color:var(--white);display:flex;padding:40px 80px 0;gap:60px}
.footer-col h4{font-size:20px;font-weight:400;letter-spacing:1px;margin-bottom:14px}
.links li{list-style:none;font-size:15px;line-height:1.75}
.links li::before{content:"›";margin-right:10px}
.contact-row{display:flex;align-items:center;gap:14px;font-size:15px;margin-bottom:16px;line-height:1.35}
.contact-row svg{flex:none}
.newsletter p{font-size:14px;line-height:1.5;width:220px}
.email-field{margin-top:12px;width:230px;height:34px;background:#666;border:1px solid #999;font-size:14px;padding:6px 10px;color:#ddd}
.btn-subscribe{display:inline-block;margin-top:20px;border:2px solid var(--white);padding:6px 20px;font-size:15px;letter-spacing:1px}
.footer-brand{margin-left:auto;text-align:center}
.footer-mark{width:120px;height:120px;border-radius:50%;background:#777;margin:0 auto}
.social{display:flex;gap:10px;justify-content:center;margin-top:24px}
.social span{width:34px;height:34px;border-radius:50%;background:var(--white)}
.columns-col1{width:200px}.columns-col2{width:300px}

.copyright{height:48px;background:var(--bar);color:#ddd;font-size:14px;display:flex;align-items:center;justify-content:center}
</style>
</head>
<body>
<header class="site-header">
  <div class="brand"><span class="brand-dot"></span><span class="brand-name">Marlow Vane Group SAS</span></div>
  <nav class="main-nav"><a class="active" href="#">HOME</a><a href="#">ABOUT US</a><a href="#">SERVICES</a><a href="#">CONTACT US</a></nav>
</header>

<section class="hero">
  <div class="hero-photo" role="img" aria-label="Businessman in a suit holding a glowing brain in open hands"></div>
  <div class="hero-copy">
    <h1 class="hero-title">LOREM IPSUM IS<br>SIMPLY DUMMY TEXT.</h1>
    <a class="btn-dark" href="#">CONTACT US</a>
  </div>
</section>

<section class="welcome">
  <h2 class="section-title">WELCOME TO MARLOW VANE GROUP SAS</h2>
  <p>Lorem Ipsum is simply dummy text of the printing and typesetting industry. Lorem Ipsum has been the industry's standard dummy text ever since the 1500s, when an unknown printer took a galley of type and scrambled it to make a type specimen book.</p>
  <a class="btn-outline" href="#">READ MORE</a>
</section>

<section class="services">
  <h2 class="section-title">SERVICES WE PROVIDE</h2>
  <div class="service-grid">
    <article class="service-card"><div class="service-photo" role="img" aria-label="Hands reviewing charts on a desk"></div><h3>Business Strategy</h3><p>Lorem Ipsum is simply dummy text of the printing and typesetting industry.</p></article>
    <article class="service-card"><div class="service-photo" role="img" aria-label="Team meeting around a table"></div><h3>Management</h3><p>Lorem Ipsum is simply dummy text of the printing and typesetting industry.</p></article>
    <article class="service-card"><div class="service-photo" role="img" aria-label="Executive presenting to colleagues"></div><h3>Executive Coaching</h3><p>Lorem Ipsum is simply dummy text of the printing and typesetting industry.</p></article>
    <article class="service-card"><div class="service-photo" role="img" aria-label="Group reviewing documents at an office table"></div><h3>Business Development</h3><p>Lorem Ipsum is simply dummy text of the printing and typesetting industry.</p></article>
  </div>
</section>

<section class="news">
  <h2 class="section-title">LATEST NEWS</h2>
  <div class="news-list">
    <article class="news-item"><div class="news-photo" role="img" aria-label="Hand touching a digital network screen"></div><div><p>Lorem Ipsum is simply dummy text.</p><span class="news-date">16 July 2016</span><p>Lorem Ipsum is simply dummy text of the printing and typesetting industry.</p><a class="more" href="#">READ MORE</a></div></article>
    <article class="news-item"><div class="news-photo" role="img" aria-label="Colleagues working together at laptops" style="background:linear-gradient(135deg,#d7dde4,#8d99a8)"></div><div><p>Lorem Ipsum is simply dummy text.</p><span class="news-date">16 July 2016</span><p>Lorem Ipsum is simply dummy text of the printing and typesetting industry.</p><a class="more" href="#">READ MORE</a></div></article>
  </div>
</section>

<section class="tweets">
  <h2 class="section-title">LATEST TWEETS</h2>
  <div class="tweet-icon"></div>
  <a class="tweet-arrow prev" href="#" aria-label="Previous"><svg width="18" height="22" viewBox="0 0 18 22"><path d="M13 3 5 11l8 8" fill="none" stroke="#fff" stroke-width="3"/></svg></a>
  <a class="tweet-arrow next" href="#" aria-label="Next"><svg width="18" height="22" viewBox="0 0 18 22"><path d="M5 3l8 8-8 8" fill="none" stroke="#fff" stroke-width="3"/></svg></a>
  <p class="tweet-body">Great insights about Orrin and Delacotte at the Data Stewardship Forum<br>http://lnk.mv/u4Tb8qP http://lnk.mv/x2Kd6Wn</p>
  <p class="tweet-author">Marlow Vane Group @MarlowVane</p>
  <p class="tweet-date">Jul 14</p>
</section>

<footer class="site-footer">
  <div class="footer-col columns-col1">
    <h4>USEFUL LINKS</h4>
    <ul class="links"><li>Home</li><li>About Us</li><li>Services</li><li>Contact Us</li></ul>
  </div>
  <div class="footer-col columns-col2">
    <h4>CONTACT INFO</h4>
    <div class="contact-row"><svg width="16" height="22" viewBox="0 0 16 22"><path d="M8 1a7 7 0 0 1 7 7c0 5-7 13-7 13S1 13 1 8a7 7 0 0 1 7-7z" fill="#fff"/><circle cx="8" cy="8" r="2.6" fill="#555"/></svg><span>14 Alder Court, Fenwick Road,<br>Northvale</span></div>
    <div class="contact-row"><svg width="18" height="18" viewBox="0 0 18 18"><path d="M4 1l3 4-2 2c1 3 3 5 6 6l2-2 4 3-2 3C8 17 1 10 1 3z" fill="#fff"/></svg><span>00 1234 5678</span></div>
    <div class="contact-row"><svg width="18" height="14" viewBox="0 0 18 14"><rect x="1" y="1" width="16" height="12" fill="none" stroke="#fff" stroke-width="2"/><path d="M1 1l8 7 8-7" fill="none" stroke="#fff" stroke-width="2"/></svg><span>hello@marlowvane.co</span></div>
  </div>
  <div class="footer-col newsletter">
    <h4>NEWSLETTER</h4>
    <p>Subscribe to stay on Marlow Vane Group</p>
    <div class="email-field">Enter Email Id</div>
    <a class="btn-subscribe" href="#">SUBSCRIBE</a>
  </div>
  <div class="footer-brand">
    <div class="footer-mark"></div>
    <div class="social"><span></span><span></span><span></span></div>
  </div>
</footer>
<div class="copyright">© Marlow Vane Group · 2016. All Rights Reserved.</div>
</body>
</html>
```